Vesk Architecture

We are a architectural design and build company working between scales 1/1000 to 1/1 we want people to understand our difference from our design experience and quality.we build hotels restourants and office spaces.Our company name is Vesk architecture to mind sustainability.

We want to write our adress phone and work spesifications on the card and we want our logo as backround.

Ps:you could find the logo adress and phone box numbers from the web:www.veskmimarlik-ornek.com

Target Market(s)

Who looks for experts.

Industry/Entity Type

Architecture

Requirements
Must have
• Design is over everything.
Should not have
• we don want it to be colorfull

```html
<!DOCTYPE html>
<html lang="tr">
<head>
<meta charset="utf-8">
<title>Vesk Mimarlık – Card</title>
<link rel="stylesheet" href="https://fonts.googleapis.com/css2?family=Cinzel:wght@400;600&family=Montserrat:wght@500&display=swap">
<style>
  :root {
    --paper: #ffffff;
    --ink: #1c1c1c;
    --panel: #bdbdbe;
    --panel-text: #ffffff;
    --label-bg: #ffffff;
    --label-text: #2a2a2a;
  }
  * { margin: 0; padding: 0; box-sizing: border-box; }
  html, body {
    width: 927px;
    height: 1200px;
    overflow: hidden;
    background: var(--paper);
  }
  .card {
    position: relative;
    width: 927px;
    height: 1200px;
    background: var(--paper);
  }
  .brand {
    position: absolute;
    left: 478px;
    top: 200px;
    color: var(--ink);
    font-family: "Montserrat", sans-serif;
    font-weight: 500;
    line-height: 1;
  }
  .brand-name {
    display: block;
    margin-left: 10px;
    font-size: 118px;
    letter-spacing: -2px;
  }
  .brand-sub {
    display: block;
    margin-top: 12px;
    font-size: 30px;
    letter-spacing: 3px;
  }
  .contact-panel {
    position: absolute;
    left: 400px;
    top: 522px;
    width: 383px;
    height: 217px;
    background: var(--panel);
    border-radius: 22px;
  }
  .street {
    position: absolute;
    left: 26px;
    top: 18px;
    color: var(--panel-text);
    font-family: "Cinzel", serif;
    font-weight: 400;
    font-size: 14.5px;
    letter-spacing: 0.2px;
    white-space: nowrap;
  }
  .label {
    position: absolute;
    left: 50%;
    transform: translateX(-50%);
    width: max-content;
    height: 27px;
    padding: 0 14px;
    background: var(--label-bg);
    color: var(--label-text);
    font-family: "Cinzel", serif;
    font-size: 9px;
    font-weight: 600;
    display: flex;
    align-items: center;
    justify-content: center;
    white-space: nowrap;
    box-shadow: 0 1px 2px rgba(0,0,0,0.18);
  }
  .label-district { top: 79px; }
  .label-phone    { top: 121px; }
  .label-email    { top: 164px; height: 28px; }
</style>
</head>
<body>
  <main class="card">
    <div class="brand">
      <span class="brand-name">vesk</span>
      <span class="brand-sub">MİMARLIK</span>
    </div>
    <section class="contact-panel">
      <p class="street">Rasimpaşa Mah. Rıhtım Cad. Lale Sok.</p>
      <p class="label label-district">NO: 7 Yeldeğirmeni Kadıköy/İstanbul</p>
      <p class="label label-phone">T. 0216 555 01 42 F. 0216 555 01 43</p>
      <p class="label label-email">E-mail: veskmimarlik@ornek.com</p>
    </section>
  </main>
</body>
</html>
```